Marlowe Bay Tours. Dolphin, Sightseeing, Sunset and private tours.

Boat tours, dolphin tours, sightseeing and excursions. I would like to use both front and back. I want to make this bright, fun and appealing to all age ranges.
Use the Chatterbook Logo, yodel circle and Peeper as well as QR code.

Our Address is 417 Tillery Creek Lane
Osprey, Florida 34871
Just 15 minutes from the Village in Siesta Key and 10 minutes from downtown Venice.

Target Market(s)

Tourist looking to go boating, see dolphin or go on a beach excursion.

Requirements
Must have
• Services Offered -
• Dolphin Tours
• Sightseeing Tours - $29.00 / Person
• Sunset Tours $49.00 / Person
• Full and Half Day Tours to Shell Island -
• Half Day Tour $375 -includes up to 6 passengers. The boat is all yours!
• Call - 941-555-0187
Nice to have
• Dolphin and Sightseeing Tours Duration - Approximately 1 1/2 to 2 hours.
• We don't do crowds.
• Website Link -
• http://www.marlowebaytripsandcruises.example/
• Chatterbook Link -
• https://www.chatterbook.example/MarloweBayTripsandCruises/
• Maybe our RoamRater logo and Chatterbook Logo.

```html
<!DOCTYPE html>
<html lang="en">
<head>
<meta charset="utf-8">
<title>Marlowe Bay Tours – Rack Card Front and Back</title>
<link rel="stylesheet" href="https://fonts.googleapis.com/css2?family=Roboto+Condensed:ital,wght@0,400;0,700;1,700&display=swap">
<style>
  :root {
    --page-bg: #eef1f4;
    --ocean-light: #2a9be0;
    --ocean-deep: #0c62a8;
    --navy: #0d3f78;
    --sun-orange: #f7a21b;
    --accent-orange: #f26a21;
    --white: #ffffff;
    --ink: #1d3557;
  }
  html, body {
    margin: 0;
    padding: 0;
    width: 1200px;
    height: 800px;
    overflow: hidden;
    background: var(--page-bg);
    font-family: "Roboto Condensed", "Arial Narrow", sans-serif;
  }
  .rack-card {
    position: absolute;
    top: 30px;
    width: 340px;
    height: 740px;
    box-shadow: 0 4px 14px rgba(0,0,0,0.18);
  }
  .rack-card--front { left: 225px; }
  .rack-card--back { left: 635px; }
  .rack-card svg { display: block; width: 340px; height: 740px; }
  .card-text { font-family: "Roboto Condensed", "Arial Narrow", sans-serif; }
  .brand-name { font-weight: 700; fill: var(--navy); }
  .headline-small { fill: var(--sun-orange); font-size: 27px; }
  .headline-large { fill: var(--white); font-size: 54px; }
  .call-line { fill: var(--sun-orange); font-size: 24px; }
  .address-line { fill: var(--white); font-size: 19px; }
  .distance-line { fill: var(--white); font-size: 13px; }
  .services-title { fill: var(--accent-orange); font-size: 21px; font-weight: 700; letter-spacing: 1px; }
  .service-item { fill: var(--white); font-size: 19px; }
  .service-note { fill: var(--white); font-size: 12.5px; }
  .duration-text { fill: var(--white); font-size: 13px; font-weight: 700; }
  .tagline { fill: var(--white); font-size: 16px; font-weight: 700; font-style: italic; }
  .link-label { fill: var(--accent-orange); font-size: 10px; }
  .link-url { fill: var(--navy); font-size: 10px; }
  .link-or { fill: var(--navy); font-size: 10px; }
</style>
</head>
<body>

<!-- FRONT SIDE -->
<section class="rack-card rack-card--front">
  <svg viewBox="0 0 340 740" xmlns="http://www.w3.org/2000/svg">
    <defs>
      <linearGradient id="front-ocean" x1="0" y1="0" x2="0" y2="1">
        <stop offset="0" stop-color="#1e8fd8"/>
        <stop offset="1" stop-color="#0e67ae"/>
      </linearGradient>
      <linearGradient id="boat-scene" x1="0" y1="0" x2="0" y2="1">
        <stop offset="0" stop-color="#7cc6ee"/>
        <stop offset="0.45" stop-color="#c9e9f5"/>
        <stop offset="0.6" stop-color="#5fc0c4"/>
        <stop offset="1" stop-color="#ece6d6"/>
      </linearGradient>
      <linearGradient id="family-scene" x1="0" y1="0" x2="0" y2="1">
        <stop offset="0" stop-color="#6aa84f"/>
        <stop offset="0.5" stop-color="#d9b08c"/>
        <stop offset="1" stop-color="#6fb6d9"/>
      </linearGradient>
      <radialGradient id="dolphin-scene" cx="0.5" cy="0.5" r="0.6">
        <stop offset="0" stop-color="#7fa9a4"/>
        <stop offset="1" stop-color="#2f7f86"/>
      </radialGradient>
    </defs>

    <rect class="card-bg" width="340" height="740" fill="url(#front-ocean)"/>

    <g class="hero-photo" role="img" aria-label="Photo of the tour boat anchored at a white sand beach with turquoise water">
      <path d="M0,40 H340 V285 C250,272 140,290 0,318 Z" fill="url(#boat-scene)"/>
    </g>
    <path class="hero-edge" d="M0,318 C140,290 250,272 340,285" fill="none" stroke="var(--white)" stroke-width="5"/>

    <path class="header-swoosh" d="M110,0 H340 V98 C290,78 215,66 110,0 Z" fill="var(--white)"/>
    <path class="header-swoosh-line" d="M110,0 C215,66 290,78 340,98" fill="none" stroke="var(--ocean-deep)" stroke-width="3"/>

    <g class="brand-mark">
      <circle cx="214" cy="38" r="9" fill="var(--sun-orange)"/>
      <text class="card-text brand-name" x="330" y="43" font-size="15" text-anchor="end">Marlowe Bay Tours</text>
    </g>

    <g class="family-photo" role="img" aria-label="Photo of a smiling family with children on the boat">
      <circle cx="258" cy="365" r="78" fill="url(#family-scene)" stroke="var(--white)" stroke-width="5"/>
    </g>
    <g class="dolphin-photo" role="img" aria-label="Photo of a dolphin surfacing beside the boat">
      <circle cx="156" cy="413" r="56" fill="url(#dolphin-scene)" stroke="var(--white)" stroke-width="5"/>
    </g>

    <text class="card-text headline-small" x="12" y="522">YOUR ADVENTURE</text>
    <text class="card-text headline-large" x="10" y="575">STARTS HERE</text>

    <line x1="12" y1="585" x2="328" y2="585" stroke="var(--white)" stroke-width="1.5"/>
    <text class="card-text call-line" x="170" y="610" text-anchor="middle">CALL  941.555.0187</text>
    <line x1="12" y1="620" x2="328" y2="620" stroke="var(--white)" stroke-width="1.5"/>

    <text class="card-text address-line" x="170" y="650" text-anchor="middle">417 Tillery Creek Lane</text>
    <text class="card-text address-line" x="170" y="675" text-anchor="middle">Osprey, Florida 34871</text>

    <text class="card-text distance-line" x="170" y="706" text-anchor="middle">Just 15 minutes from the Village in Siesta Key</text>
    <text class="card-text distance-line" x="170" y="723" text-anchor="middle">and 10 minutes from downtown Venice</text>
  </svg>
</section>

<!-- BACK SIDE -->
<section class="rack-card rack-card--back">
  <svg viewBox="0 0 340 740" xmlns="http://www.w3.org/2000/svg">
    <defs>
      <linearGradient id="back-ocean" x1="0" y1="0" x2="0" y2="1">
        <stop offset="0" stop-color="#1a88d2"/>
        <stop offset="1" stop-color="#2da3e6"/>
      </linearGradient>
      <linearGradient id="group-scene" x1="0" y1="0" x2="0" y2="1">
        <stop offset="0" stop-color="#8ccff2"/>
        <stop offset="0.45" stop-color="#d8b494"/>
        <stop offset="1" stop-color="#56bcc0"/>
      </linearGradient>
      <linearGradient id="shore-scene" x1="0" y1="0" x2="0" y2="1">
        <stop offset="0" stop-color="#6bb9ea"/>
        <stop offset="0.55" stop-color="#bfe3f3"/>
        <stop offset="1" stop-color="#2f8fc4"/>
      </linearGradient>
    </defs>

    <rect class="card-bg" width="340" height="740" fill="url(#back-ocean)"/>

    <g class="group-photo" role="img" aria-label="Photo of a group of friends standing in shallow water">
      <circle cx="92" cy="92" r="100" fill="url(#group-scene)" stroke="var(--white)" stroke-width="5"/>
    </g>
    <g class="shore-photo" role="img" aria-label="Photo of a quiet island shoreline">
      <circle cx="225" cy="140" r="54" fill="url(#shore-scene)" stroke="var(--white)" stroke-width="5"/>
    </g>

    <g class="services-tag">
      <rect x="96" y="206" width="204" height="32" fill="var(--white)"/>
      <rect x="96" y="238" width="204" height="4" fill="var(--sun-orange)"/>
      <text class="card-text services-title" x="198" y="229" text-anchor="middle">SERVICES OFFERED</text>
    </g>

    <g class="services-list">
      <circle cx="36" cy="283" r="3.5" fill="var(--accent-orange)"/>
      <text class="card-text service-item" x="46" y="289">Dolphin Tours</text>
      <circle cx="36" cy="318" r="3.5" fill="var(--accent-orange)"/>
      <text class="card-text service-item" x="46" y="324">Sightseeing Tours—$29.00 / Person</text>
      <circle cx="36" cy="353" r="3.5" fill="var(--accent-orange)"/>
      <text class="card-text service-item" x="46" y="359">Sunset Tours $49.00 / Person</text>
      <circle cx="36" cy="388" r="3.5" fill="var(--accent-orange)"/>
      <text class="card-text service-item" x="46" y="394">Full and Half Day Tours to Shell Island</text>
      <circle cx="36" cy="423" r="3.5" fill="var(--accent-orange)"/>
      <text class="card-text service-item" x="46" y="429">Half Day Tour $375</text>
      <text class="card-text service-note" x="46" y="447">(Includes up to 6 passengers. The boat is all yours!)</text>
    </g>

    <g class="duration-tag">
      <rect x="18" y="468" width="246" height="46" rx="4" fill="var(--sun-orange)"/>
      <text class="card-text duration-text" x="141" y="487" text-anchor="middle">Dolphin and Sightseeing Tours Duration—</text>
      <text class="card-text duration-text" x="141" y="504" text-anchor="middle">Approximately 1 1/2 to 2 hours</text>
    </g>

    <text class="card-text tagline" x="170" y="546" text-anchor="middle">We don't do crowds!</text>

    <path class="footer-wave" d="M0,572 C90,600 220,590 340,560 V740 H0 Z" fill="var(--white)"/>

    <g class="brand-mark">
      <circle cx="170" cy="632" r="14" fill="var(--sun-orange)"/>
      <text class="card-text brand-name" x="170" y="670" font-size="22" text-anchor="middle">Marlowe Bay Tours</text>
    </g>

    <text class="card-text" x="170" y="697" text-anchor="middle">
      <tspan class="link-label">VISIT US AT: </tspan><tspan class="link-url">http://www.marlowebaytripsandcruises.example/</tspan>
    </text>
    <line x1="100" y1="709" x2="155" y2="709" stroke="var(--navy)" stroke-width="0.7"/>
    <text class="card-text link-or" x="170" y="712" text-anchor="middle">OR</text>
    <line x1="185" y1="709" x2="240" y2="709" stroke="var(--navy)" stroke-width="0.7"/>

    <circle class="social-dot" cx="28" cy="726" r="8" fill="var(--navy)"/>
    <text class="card-text link-url" x="42" y="730">https://www.chatterbook.example/MarloweBayTripsandCruises/</text>
  </svg>
</section>

</body>
</html>
```